Classic Rock covers band needs a gig poster

We are a UK based classic rock covers band and we need a poster for our gigs. The poster needs to clearly identify the band in the correct genre - classic rock / country rock.We are interested in seeing innovative designs that match the music genre we play. Please note, we are NOT a metal band, but a rock band and all such designs should reflect this.Original illustrations or photo concepts that fit the classic rock genre are welcomed.The name of the band is Copper Lantern and this should be clearly visible at the top of the poster.Included with this post is an image of our current logo and a rough layout file to give you and idea of what we're after.The band logo can be updated, but any new logo should be clear and easy to read.

Target Market(s)

Music venues, pubs

Font styles to use
Serif
Sans Serif
Decorative
Script

Requirements
Must have
• Images or illustrations that demonstrate to the viewer the band is a classic rock covers band.
Nice to have
• It would be nice to see some variation on the letter styling of the band name. In addition it would be nice to see original drawings / artwork that are "classic rock" related.

```html
<!DOCTYPE html>
<html lang="en">
<head>
<meta charset="utf-8">
<title>Copper Lantern – Gig Poster</title>
<link rel="stylesheet" href="https://fonts.googleapis.com/css2?family=Rye&family=Playfair+Display:wght@900&family=Josefin+Sans:wght@600;700&display=swap">
<style>
  :root {
    --brown: #6d3a2b;
    --tan: #d8a665;
    --tan-light: #e2b57a;
    --tan-pale: #ebc791;
    --amber: #fbb040;
    --red: #b01116;
    --lilac: #857c9f;
    --white: #ffffff;
  }
  html, body {
    margin: 0;
    padding: 0;
    overflow: hidden;
    background: var(--brown);
  }
  .poster {
    position: relative;
    width: 848px;
    height: 1200px;
    overflow: hidden;
    background: var(--brown);
  }
  .poster-art {
    position: absolute;
    inset: 0;
    width: 848px;
    height: 1200px;
    display: block;
  }
  .band-name {
    font-family: "Rye", serif;
    fill: var(--red);
  }
  .band-tag {
    font-family: "Playfair Display", serif;
    font-weight: 900;
    fill: var(--white);
    letter-spacing: -1px;
  }
  .gig-date,
  .gig-venue {
    font-family: "Josefin Sans", sans-serif;
    font-weight: 700;
    fill: var(--lilac);
  }
</style>
</head>
<body>
<main class="poster">
  <svg class="poster-art" viewBox="0 0 848 1200" xmlns="http://www.w3.org/2000/svg">
    <defs>
      <radialGradient id="arch-glow" cx="50%" cy="62%" r="60%">
        <stop offset="0" stop-color="#f0d09e"/>
        <stop offset="1" stop-color="var(--tan-light)"/>
      </radialGradient>
      <radialGradient id="wing-tone" cx="50%" cy="50%" r="55%">
        <stop offset="0" stop-color="#f7a238"/>
        <stop offset="1" stop-color="#e8602a"/>
      </radialGradient>
      <linearGradient id="guitar-tone" x1="0" y1="0" x2="0" y2="1">
        <stop offset="0" stop-color="#b8322c"/>
        <stop offset="0.55" stop-color="#d9702a"/>
        <stop offset="1" stop-color="#f2c21e"/>
      </linearGradient>
    </defs>

    <!-- edge bands -->
    <g class="edge-bands" fill="var(--tan)">
      <rect x="0" y="0" width="848" height="12"/>
      <rect x="0" y="1188" width="848" height="12"/>
      <polygon points="0,0 90,0 0,60"/>
      <polygon points="848,0 758,0 848,60"/>
      <polygon points="0,1200 90,1200 0,1140"/>
      <polygon points="848,1200 758,1200 848,1140"/>
      <rect x="0" y="240" width="22" height="60"/>
      <rect x="0" y="440" width="22" height="60"/>
      <rect x="0" y="640" width="22" height="60"/>
      <rect x="0" y="840" width="22" height="60"/>
      <rect x="826" y="240" width="22" height="60"/>
      <rect x="826" y="440" width="22" height="60"/>
      <rect x="826" y="640" width="22" height="60"/>
      <rect x="826" y="840" width="22" height="60"/>
    </g>

    <!-- frame lines -->
    <g class="frame" fill="none" stroke="var(--tan)">
      <rect x="20" y="26" width="808" height="1148" stroke-width="4"/>
      <rect x="48" y="58" width="752" height="1086" stroke-width="2"/>
    </g>
    <g class="frame-bars" fill="var(--tan)">
      <rect x="128" y="60" width="100" height="6"/>
      <rect x="620" y="60" width="100" height="6"/>
      <rect x="128" y="80" width="100" height="6"/>
      <rect x="620" y="80" width="100" height="6"/>
      <rect x="128" y="1118" width="100" height="6"/>
      <rect x="620" y="1118" width="100" height="6"/>
      <rect x="64" y="160" width="4" height="880"/>
      <rect x="780" y="160" width="4" height="880"/>
    </g>

    <!-- guitar illustration areas -->
    <rect role="img" aria-label="Acoustic guitar illustration, headstock up, tilted left" x="70" y="30" width="110" height="300" rx="40"
          fill="url(#guitar-tone)" transform="rotate(-30 125 180)"/>
    <rect role="img" aria-label="Acoustic guitar illustration, headstock up, tilted right" x="668" y="30" width="110" height="300" rx="40"
          fill="url(#guitar-tone)" transform="rotate(30 723 180)"/>

    <!-- pointed arch -->
    <path class="arch-outer" fill="var(--tan)"
          d="M424 62 C650 180 820 420 804 700 C792 900 610 1080 424 1182 C238 1080 56 900 44 700 C28 420 198 180 424 62Z"/>
    <path class="arch-dots" fill="none" stroke="var(--brown)" stroke-width="4" stroke-dasharray="4 8"
          d="M424 98 C630 210 790 430 774 700 C762 890 596 1055 424 1150 C252 1055 86 890 74 700 C58 430 218 210 424 98Z"/>
    <path class="arch-inner-dots" fill="none" stroke="var(--brown)" stroke-width="3" stroke-dasharray="4 8"
          d="M424 160 C610 260 742 455 726 700 C716 890 578 1005 424 1092 C270 1005 132 890 122 700 C106 455 238 260 424 160Z"/>
    <path class="arch-inner" fill="url(#arch-glow)" stroke="var(--brown)" stroke-width="3"
          d="M424 180 C596 272 722 462 708 700 C700 880 570 990 424 1070 C278 990 148 880 140 700 C126 462 252 272 424 180Z"/>

    <!-- band name -->
    <text class="band-name" x="34" y="548" font-size="176" textLength="776" lengthAdjust="spacingAndGlyphs">COPPER</text>
    <text class="band-name" x="150" y="688" font-size="150" textLength="500" lengthAdjust="spacingAndGlyphs">LANTERN</text>
    <text class="band-tag" x="416" y="740" font-size="32" text-anchor="middle" textLength="222" lengthAdjust="spacingAndGlyphs">COVER BAND</text>

    <!-- ribbon tails -->
    <g class="ribbon-tails" fill="var(--amber)">
      <polygon points="50,958 215,905 215,990 110,1012 122,968"/>
      <polygon points="798,958 633,905 633,990 738,1012 726,968"/>
    </g>

    <!-- date banner -->
    <rect class="banner" x="123" y="773" width="601" height="122" fill="var(--amber)" stroke="var(--brown)" stroke-width="5"/>
    <text class="gig-date" x="424" y="842" font-size="44" text-anchor="middle" textLength="506" lengthAdjust="spacingAndGlyphs">SATURDAY. 10TH  MARCH</text>
    <text class="gig-venue" x="424" y="878" font-size="26" text-anchor="middle" textLength="298" lengthAdjust="spacingAndGlyphs">AT MILLBROOK STADIUM</text>

    <!-- winged star illustration area -->
    <ellipse role="img" aria-label="Copper star with spread orange feathered wings"
             cx="424" cy="1040" rx="270" ry="100" fill="url(#wing-tone)"/>
  </svg>
</main>
</body>
</html>
```